Need a banner designed to help prank my neighbor.

I'm looking for creativity and fun in a banner that I will hang on a large tree outside my house facing a neighbor. He just started decorating for Christmas and I always joke with him that it is too early. This is a fun project. Nothing too serious. I welcome your skills to make it awesome.

I have the basics of a sign designed (attached), but I need it brought to the next level with better font and images.

Banner will be printed at 4-feet x 8-feet.
Top part of my mock up is most important to see/read easily.

```html
<!DOCTYPE html>
<html lang="en">
<head>
<meta charset="utf-8">
<title>Stop Premature Christmas Decoratings — Banner</title>
<link href="https://fonts.googleapis.com/css2?family=Poppins:wght@500;800;900&family=Fira+Sans+Extra+Condensed:wght@800&display=swap" rel="stylesheet">
<style>
  :root {
    --backdrop: #d6d6d6;
    --paper: #ededed;
    --ink: #000000;
    --holiday-red: #a4000f;
    --light: #eeeeee;
    --pill: #f4f4f4;
  }
  html, body {
    margin: 0;
    padding: 0;
    width: 1200px;
    height: 767px;
    overflow: hidden;
    background: var(--backdrop);
  }
  .canvas {
    display: block;
    width: 1200px;
    height: 767px;
  }
  .canvas__bg { fill: var(--backdrop); }
  .banner__bg { fill: var(--paper); }
  .headline-letter {
    font-family: "Poppins", sans-serif;
    font-weight: 900;
    font-size: 362px;
    fill: var(--ink);
  }
  .emblem-area { fill: var(--holiday-red); }
  .subhead {
    font-family: "Poppins", sans-serif;
    font-weight: 800;
    font-size: 42px;
    fill: var(--ink);
  }
  .footer-band { fill: var(--holiday-red); }
  .slogan {
    font-family: "Fira Sans Extra Condensed", sans-serif;
    font-weight: 800;
    font-size: 104px;
    fill: var(--light);
  }
  .hashtag__pill { fill: var(--pill); }
  .hashtag__text {
    font-family: "Poppins", sans-serif;
    font-weight: 500;
    font-size: 24px;
    fill: var(--ink);
  }
</style>
</head>
<body>
<svg class="canvas" viewBox="0 0 1200 767" xmlns="http://www.w3.org/2000/svg">
  <rect class="canvas__bg" width="1200" height="767"/>

  <g class="banner" transform="translate(0,83)">
    <rect class="banner__bg" width="1200" height="600"/>

    <!-- Headline: STOP, with an emblem standing in for the O -->
    <text class="headline-letter" x="76" y="306" textLength="211" lengthAdjust="spacingAndGlyphs">S</text>
    <text class="headline-letter" x="322" y="306" textLength="224" lengthAdjust="spacingAndGlyphs">T</text>
    <rect class="emblem-area" x="562" y="60" width="296" height="244" rx="28"
          role="img" aria-label="Red stop-sign emblem with a Christmas tree, forming the O of STOP"/>
    <text class="headline-letter" x="902" y="306" textLength="220" lengthAdjust="spacingAndGlyphs">P</text>

    <!-- Arched subhead -->
    <path id="subhead-arc" d="M81,384 Q600,322 1118,379" fill="none"/>
    <text class="subhead">
      <textPath href="#subhead-arc" textLength="1037" lengthAdjust="spacingAndGlyphs">PREMATURE CHRISTMAS DECORATINGS</textPath>
    </text>

    <!-- Footer band -->
    <path class="footer-band" d="M0,409 Q600,317 1200,409 V600 H0 Z"/>

    <text class="slogan" x="76" y="502" textLength="1049" lengthAdjust="spacingAndGlyphs">THANKSGIVING FIRST.</text>

    <g class="hashtags">
      <rect class="hashtag__pill" x="79" y="518" width="412" height="36" rx="8"/>
      <text class="hashtag__text" x="90" y="544" textLength="390" lengthAdjust="spacingAndGlyphs">#ligtsgoupafterthanksgiving</text>

      <rect class="hashtag__pill" x="500" y="518" width="338" height="36" rx="8"/>
      <text class="hashtag__text" x="511" y="544" textLength="316" lengthAdjust="spacingAndGlyphs">#savethebabyreindeer</text>

      <rect class="hashtag__pill" x="847" y="518" width="274" height="36" rx="8"/>
      <text class="hashtag__text" x="858" y="544" textLength="252" lengthAdjust="spacingAndGlyphs">#lookingatyou2418</text>
    </g>
  </g>
</svg>
</body>
</html>
```